Corvallin Property Solutions need a business card design

Hello guys. We would need a business card design asap please.
We are a start up property investment business based in London UK specialised in buying, selling, managing and letting properties and helping distressed property owners.
The name of our Business is Corvallin, the logo symbolises the four fundamental elements of the world (earth, air, fire and water) and so it stands for strength, stability, longevity.
We would like the business card to communicate professionalism and reliability. Many many thanks indeed for your work.

Details:

1.) Marisol Dunkley
Property Investor
Mobile: +44(0)7700362517
Email: marisol.corvallin@quilbrook.example

2.) Tomas Brindle
Property Investor
Mobile: +44(0)7700845926
Email: tomas.corvallin@quilbrook.example

Industry/Entity Type

Investment

```html
<!DOCTYPE html>
<html lang="en">
<head>
<meta charset="utf-8">
<title>Corvallin Property Solutions – Business Card</title>
<link rel="stylesheet" href="https://fonts.googleapis.com/css2?family=Lato:wght@400;700;900&display=swap">
<style>
  :root {
    --backdrop: #e9e7e4;
    --card-white: #ffffff;
    --card-black: #1c1c1c;
    --pattern-dark: #161616;
    --pattern-light: #2e2e2e;
    --ink: #1a1a1a;
    --ink-soft: #4a4a4a;
    --brand-green: #1fa463;
    --brand-blue: #2f8fd0;
    --brand-red: #e0323f;
    --rule: #d8d8d8;
  }
  * { box-sizing: border-box; margin: 0; padding: 0; }
  html, body {
    width: 1200px; height: 800px; overflow: hidden;
    background: var(--backdrop);
    font-family: "Lato", Arial, sans-serif;
  }
  .canvas { position: relative; width: 1200px; height: 800px; }

  /* Back of card */
  .card-back {
    position: absolute; left: 110px; top: 120px;
    width: 330px; height: 560px;
    background: var(--card-black);
    box-shadow: 0 10px 30px rgba(0,0,0,.25);
    overflow: hidden;
  }
  .card-back__pattern {
    position: absolute; inset: 0;
    background: linear-gradient(160deg, var(--pattern-light), var(--pattern-dark) 70%);
  }
  .card-back__brand {
    position: absolute; left: 200px; top: 230px;
    transform-origin: left top; transform: rotate(90deg);
    color: #d9d9d9; white-space: nowrap;
  }
  .card-back__name {
    font-weight: 900; font-size: 44px; letter-spacing: 2px; line-height: 1;
  }
  .card-back__tagline {
    font-weight: 700; font-size: 18px; letter-spacing: 2px; margin-top: 6px;
  }

  /* Front of card */
  .card-front {
    position: absolute; left: 500px; top: 220px;
    width: 620px; height: 360px;
    background: var(--card-white);
    box-shadow: 0 10px 30px rgba(0,0,0,.25);
    overflow: hidden;
  }
  .brand {
    position: absolute; left: 48px; top: 56px; color: var(--ink);
  }
  .brand__mark { display: flex; align-items: center; gap: 10px; }
  .brand__square { width: 18px; height: 18px; background: var(--ink); }
  .brand__name {
    font-weight: 900; font-size: 30px; letter-spacing: 1.5px; line-height: 1;
  }
  .brand__tagline {
    font-weight: 400; font-size: 12px; letter-spacing: 1.5px;
    margin-top: 6px; margin-left: 28px; color: var(--ink-soft);
  }
  .divider {
    position: absolute; left: 0; top: 0; width: 620px; height: 340px;
  }
  .contact {
    position: absolute; left: 330px; top: 150px; color: var(--ink);
  }
  .contact__name {
    font-weight: 900; font-size: 24px; letter-spacing: 1.5px; text-transform: uppercase;
  }
  .contact__role { font-size: 14px; color: var(--ink-soft); margin: 4px 0 14px; }
  .contact__line {
    display: flex; align-items: center; gap: 8px;
    font-size: 14px; margin-bottom: 6px;
  }
  .contact__icon { width: 14px; height: 14px; flex: none; }
  .colour-band {
    position: absolute; left: 0; bottom: 0; width: 100%; height: 20px; display: flex;
  }
  .colour-band span { height: 100%; }
  .band-black { flex: 310; background: var(--card-black); }
  .band-green { flex: 100; background: var(--brand-green); }
  .band-blue  { flex: 100; background: var(--brand-blue); }
  .band-red   { flex: 110; background: var(--brand-red); }
</style>
</head>
<body>
<main class="canvas">

  <section class="card-back" aria-label="Card back">
    <div class="card-back__pattern" role="img" aria-label="Dark triangular tessellation pattern"></div>
    <div class="card-back__brand">
      <div class="card-back__name">CORVALLIN</div>
      <div class="card-back__tagline">PROPERTY SOLUTIONS</div>
    </div>
  </section>

  <section class="card-front" aria-label="Card front">
    <div class="brand">
      <div class="brand__mark">
        <span class="brand__square"></span>
        <span class="brand__name">CORVALLIN</span>
      </div>
      <div class="brand__tagline">PROPERTY SOLUTIONS</div>
    </div>

    <svg class="divider" viewBox="0 0 620 340" aria-hidden="true">
      <line x1="310" y1="130" x2="230" y2="340" stroke="var(--rule)" stroke-width="1"/>
    </svg>

    <div class="contact">
      <div class="contact__name">Marisol Dunkley</div>
      <div class="contact__role">Property Investor</div>
      <div class="contact__line">
        <svg class="contact__icon" viewBox="0 0 14 14" aria-hidden="true">
          <rect width="14" height="14" rx="2" fill="var(--brand-red)"/>
          <rect x="4.5" y="2.5" width="5" height="9" rx="1" fill="none" stroke="#fff" stroke-width="1.2"/>
          <circle cx="7" cy="9.8" r=".7" fill="#fff"/>
        </svg>
        <span>+44(0)7700362517</span>
      </div>
      <div class="contact__line">
        <svg class="contact__icon" viewBox="0 0 14 14" aria-hidden="true">
          <rect width="14" height="14" rx="2" fill="var(--brand-red)"/>
          <rect x="2.5" y="4" width="9" height="6.5" fill="none" stroke="#fff" stroke-width="1.2"/>
          <polyline points="2.5,4 7,8 11.5,4" fill="none" stroke="#fff" stroke-width="1.2"/>
        </svg>
        <span>marisol.corvallin@quilbrook.example</span>
      </div>
    </div>

    <div class="colour-band" aria-hidden="true">
      <span class="band-black"></span>
      <span class="band-green"></span>
      <span class="band-blue"></span>
      <span class="band-red"></span>
    </div>
  </section>

</main>
</body>
</html>
```